Business Card Design Project

We require a professional business card designed for our consulting organisation that has the same theme and colours as our logo except for the grey.

Colours on the front should predominately be white however some reference to our logo colours except for the grey.

The back of the card should be have background colour that aligns with our logo colour.

Layout, style and design is up to the designer. So send through your designs

Details are attached in the word document project brief.

Target Market(s)

Target market are large corporate organisations

Industry/Entity Type

Business

Requirements
Must have
• Content on the front must have:

Dale Fenwick
Managing Director

P: 0412 557 208
E: Dale@braviotraxgroup.com
W: www.braviotraxgroup.com

Content on the back must have the words:
Alliances
Placement
Training
Support

Design Colours
Must align to our logo

```html
<!DOCTYPE html>
<html lang="en">
<head>
<meta charset="utf-8">
<title>BravioTrax Group – Business Card</title>
<link rel="stylesheet" href="https://fonts.googleapis.com/css2?family=Oxygen:wght@400;700&display=swap">
<style>
  :root {
    --brand-blue: #1a73c2;
    --brand-blue-deep: #0f64b3;
    --brand-blue-light: #2a8ad4;
    --wash: #e9f2fa;
    --paper: #ffffff;
    --ink: #1f1f1f;
  }
  html, body {
    margin: 0;
    padding: 0;
    width: 1200px;
    height: 686px;
    overflow: hidden;
    background: var(--paper);
  }
  .card {
    position: relative;
    width: 1200px;
    height: 686px;
    background: var(--paper);
    font-family: "Oxygen", "Tahoma", sans-serif;
    color: var(--ink);
    overflow: hidden;
  }
  .backdrop-disc {
    position: absolute;
    left: 610px;
    top: 20px;
    width: 860px;
    height: 860px;
    border-radius: 50%;
    background: var(--wash);
  }
  .feature-disc {
    position: absolute;
    left: 168px;
    top: 60px;
    width: 206px;
    height: 206px;
    border-radius: 50%;
    background: linear-gradient(135deg, var(--brand-blue-deep), var(--brand-blue-light));
  }
  .brand-lockup {
    position: absolute;
    left: 756px;
    top: 48px;
    display: flex;
    align-items: center;
    gap: 26px;
  }
  .brand-lockup__dot {
    width: 96px;
    height: 96px;
    border-radius: 50%;
    background: var(--brand-blue);
  }
  .brand-lockup__name {
    font-size: 41px;
    font-weight: 700;
    line-height: 1.02;
    color: var(--brand-blue);
    letter-spacing: 0.5px;
  }
  .name-band {
    position: absolute;
    left: 0;
    top: 349px;
    width: 533px;
    height: 120px;
    background: linear-gradient(90deg, var(--brand-blue-deep), var(--brand-blue-light) 45%, var(--brand-blue-deep));
    border-radius: 0 14px 14px 0;
  }
  .name-band__rule {
    position: absolute;
    left: 53px;
    top: 22px;
    width: 2px;
    height: 80px;
    background: var(--paper);
  }
  .name-band__name {
    position: absolute;
    left: 102px;
    top: 16px;
    margin: 0;
    font-size: 48px;
    font-weight: 400;
    color: var(--paper);
    white-space: nowrap;
  }
  .name-band__title {
    position: absolute;
    right: 86px;
    top: 72px;
    margin: 0;
    font-size: 21px;
    font-weight: 400;
    color: var(--paper);
    white-space: nowrap;
  }
  .contact {
    position: absolute;
    left: 54px;
    top: 551px;
    margin: 0;
    font-size: 23px;
    line-height: 30px;
  }
  .contact__row {
    display: flex;
  }
  .contact__label {
    width: 81px;
  }
  .contact__sep {
    width: 18px;
  }
  .contact__value {
    margin: 0;
  }
</style>
</head>
<body>
  <div class="card">
    <div class="backdrop-disc" aria-hidden="true"></div>
    <div class="feature-disc" aria-hidden="true"></div>

    <div class="brand-lockup">
      <span class="brand-lockup__dot"></span>
      <span class="brand-lockup__name">BravioTrax<br>Group</span>
    </div>

    <div class="name-band">
      <span class="name-band__rule"></span>
      <h1 class="name-band__name">Dale Fenwick</h1>
      <p class="name-band__title">Managing Director</p>
    </div>

    <dl class="contact">
      <div class="contact__row"><dt class="contact__label">Phone</dt><span class="contact__sep">:</span><dd class="contact__value">0412 557 208</dd></div>
      <div class="contact__row"><dt class="contact__label">Email</dt><span class="contact__sep">:</span><dd class="contact__value">Dale@braviotraxgroup.com</dd></div>
      <div class="contact__row"><dt class="contact__label">Web</dt><span class="contact__sep">:</span><dd class="contact__value">www.braviotraxgroup.com</dd></div>
    </dl>
  </div>
</body>
</html>
```